Orbix Watch app inspired by the Ember Thermostat

Balmora allows you to control your Ember Thermostat from your Orbix Wrist device (Vortal Watch).
The UI consists of two screens, phone and device, and the design will resemble the Ember look and feel (do not exactly copy, I need something that looks similar). The thermostat control will be front and center, with a white background and blue highlights.
A logo is also needed (custom typography is a plus).

My app is live in the Orbix Fetch Market at:
fetch.vortalia.net/store/apps/details?id=com.brightkiln.balmora

The app currently supports the following devices:

The RU Vtime:
https://fetch.vortalia.net/store/devices/details?id=ru_v_time_black

The Halvorn Cog Spark:
https://fetch.vortalia.net/store/devices/details?id=halvorn_cog_spark_black

Target Market(s)

Vortal Watch wearers who have a Ember at home.

Industry/Entity Type

Orbix

Colors
33a6d7
0555a3
3176b5
fefefe
85acd3
ffffff
cee9f5
cedeec
fbc994

Requirements
Must have
• Two screen designs:
• 1. A 1080 x 1920 px layout for orbix phones.
• 2. A 320 x 320 px layout for Orbix Wrist devices (please Vortal "RU V Watch" or "Halvorn Cog Spark" for a visual of the devices I support).
• Design should resemble the Ember experience at emberhaus.net. Using similar fonts, theme and shapes is a must. Please don't copy and paste elements. I need your interpretation of the UI, not the exact same elements from Ember.
• Please look at the screenshots of the Ember Orbix app for inspiration:
• https://fetch.vortalia.net/store/apps/details?id=com.emberworks.orbix&hl=en
Nice to have
• The project consists of two rather simple layouts, so I'm asking for a logo for my app as well.
Should not have
• No black/dark backgrounds, no square buttons. Please approach the Ember look and feel as much as possible, especially in the VTime design.
• This should go without saying but:
• DO NOT copy paste elements from the Ember page. DO NOT plagiarize other peoples logos or artwork.
• Only original design work will win the contest.

```html
<!DOCTYPE html>
<html lang="en">
<head>
<meta charset="utf-8">
<title>Balmora – Phone Screen</title>
<link rel="stylesheet" href="https://fonts.googleapis.com/css2?family=Roboto:wght@300;400;500&family=Open+Sans:wght@600&display=swap">
<style>
  :root {
    --stage: #353535;
    --screen-bg: #f3f6f9;
    --header-blue: #3a8fe2;
    --header-blue-deep: #2f7fd6;
    --dial-blue: #3176b5;
    --dial-dark: #0555a3;
    --number-blue: #2f8ee0;
    --control-grey: #b9bec4;
    --white: #ffffff;
    --roof-tan: #d6a56d;
    --roof-light: #e0b47f;
    --tree-green: #35c33b;
    --label-brown: #6b4424;
    --nav-black: #050505;
    --nav-icon: #d8d8d8;
  }
  * { margin: 0; padding: 0; box-sizing: border-box; }
  html, body {
    width: 1200px; height: 900px; overflow: hidden;
    background: var(--stage);
    font-family: "Roboto", Arial, sans-serif;
  }
  .phone-screen {
    position: absolute; left: 370px; top: 40px;
    width: 460px; height: 818px;
    background: var(--screen-bg);
    overflow: hidden;
  }
  .app-header {
    position: absolute; left: -60px; top: -120px;
    width: 580px; height: 290px;
    border-radius: 50%;
    background: linear-gradient(180deg, var(--header-blue-deep), var(--header-blue));
  }
  .status-bar {
    position: absolute; top: 0; left: 0; right: 0; height: 24px;
    display: flex; justify-content: flex-end; align-items: center; gap: 6px;
    padding-right: 10px; color: var(--white); font-size: 12px;
  }
  .status-icon { width: 9px; height: 9px; background: var(--white); }
  .status-icon.wifi { clip-path: polygon(0 0, 100% 0, 50% 100%); }
  .status-icon.signal { clip-path: polygon(100% 0, 100% 100%, 0 100%); }
  .status-icon.battery { width: 6px; height: 11px; }
  .app-brand {
    position: absolute; top: 66px; left: 0; right: 0;
    display: flex; justify-content: center; align-items: center; gap: 9px;
    color: var(--white); font-size: 30px; font-weight: 500; letter-spacing: 0.5px;
  }
  .brand-dot { width: 14px; height: 14px; border-radius: 50%; background: var(--white); }
  .thermostat-dial {
    position: absolute; left: 95px; top: 160px; width: 270px; height: 270px;
  }
  .dial-controls {
    position: absolute; left: 95px; top: 160px; width: 270px; height: 270px;
  }
  .dial-plus, .dial-minus {
    position: absolute; left: 78px; color: var(--control-grey);
    font-size: 32px; font-weight: 300;
  }
  .dial-plus { top: 58px; }
  .dial-minus { top: 172px; left: 140px; }
  .setpoint {
    position: absolute; left: 80px; top: 84px;
    color: var(--number-blue); font-weight: 400; font-size: 78px; line-height: 1;
    display: flex; align-items: flex-start;
  }
  .setpoint-fraction { font-size: 22px; margin-left: 6px; margin-top: 4px; }
  .room-scene {
    position: absolute; left: 0; top: 560px; width: 460px; height: 200px;
    background: linear-gradient(180deg, var(--roof-light), var(--roof-tan));
  }
  .room-scene .tree-area {
    position: absolute; left: 0; top: 0; width: 110px; height: 200px;
    background: var(--tree-green); border-radius: 0 55px 0 0;
  }
  .room-label {
    position: absolute; left: 210px; top: 640px; width: 190px;
    text-align: center; color: var(--label-brown);
    font-family: "Open Sans", Arial, sans-serif; font-weight: 600; font-size: 15px; letter-spacing: 0.5px;
  }
  .nav-bar {
    position: absolute; left: 0; bottom: 0; width: 100%; height: 58px;
    background: var(--nav-black);
    display: flex; justify-content: space-around; align-items: center; padding: 0 50px;
  }
</style>
</head>
<body>
  <main class="phone-screen">
    <div class="app-header"></div>
    <div class="status-bar">
      <span class="status-icon wifi"></span>
      <span class="status-icon signal"></span>
      <span class="status-icon battery"></span>
      <span class="status-time">13:45</span>
    </div>
    <div class="app-brand"><span class="brand-dot"></span><span class="brand-name">Balmora</span></div>

    <svg class="thermostat-dial" viewBox="0 0 270 270" aria-hidden="true">
      <circle cx="135" cy="135" r="118" fill="none" stroke="var(--dial-blue)" stroke-width="26"
              pathLength="360" stroke-dasharray="0.6 1.4" opacity="0.85"/>
      <path d="M135 135 L290 180 L290 300 L135 300 Z" fill="var(--screen-bg)"/>
      <path d="M 211 45 A 118 118 0 0 1 240 82" fill="none" stroke="var(--dial-dark)"
            stroke-width="26" stroke-dasharray="1.2 2.2"/>
    </svg>
    <div class="dial-controls">
      <span class="dial-plus">+</span>
      <div class="setpoint"><span class="setpoint-whole">78</span><span class="setpoint-fraction">75</span></div>
      <span class="dial-minus">–</span>
    </div>

    <div class="room-scene" role="img" aria-label="Flat illustration of a house roof with a chimney and a tree, marking the living room">
      <div class="tree-area"></div>
    </div>
    <div class="room-label">LIVING ROOM</div>

    <nav class="nav-bar">
      <svg width="24" height="22" viewBox="0 0 24 22" aria-label="Back"><path d="M3 11 L21 2 L21 20 Z" fill="none" stroke="var(--nav-icon)" stroke-width="2"/></svg>
      <svg width="24" height="24" viewBox="0 0 24 24" aria-label="Home"><circle cx="12" cy="12" r="10" fill="none" stroke="var(--nav-icon)" stroke-width="2"/></svg>
      <svg width="22" height="22" viewBox="0 0 22 22" aria-label="Recent apps"><rect x="2" y="2" width="18" height="18" fill="none" stroke="var(--nav-icon)" stroke-width="2"/></svg>
    </nav>
  </main>
</body>
</html>
```